Business card design needed

We need a business card design for a new consulting business based in Melbourne called Harbor Ridge Advisory. Our tag line is 'Foundations For Your Mission'. We work with not for profits and Small - Medium Enterprises to provide advice and solutions around finance, governance, HR, IT and risk management. The idea around our organisation is to help charities and small businesses with their business foundations, so that they can spend more time focussing on their mission.
We have a logo designed already and would like the business card to use similar colours and themes - collaboration, having a conversation, creating impact. We would like the design to be eye catching but also convey professional credibility.
We would like a double sided card please.
Target Market(s)
CEOs and senior managers in charities and Small to Medium Enterprises
Industry/Entity Type
Business
Contact Information for Business Card
Business Name: Harbor Ridge Advisory
Staff Member: Janet Colby FCA
Title: Principal Consultant
Email address: janet@harborridgeadvisory.com.au
Phone: 03 9871 2264
Mobile: 0412 846 309
Address: PO Box 87, Larkfield VIC 3148
Web: www.harborridgeadvisory.com.au
Linked In: au.linkedin.com/in/janetcolbyhra/
Look and feel

```html
<!DOCTYPE html>
<html lang="en">
<head>
<meta charset="utf-8">
<title>Harbor Ridge Advisory – Business Card</title>
<link href="https://fonts.googleapis.com/css2?family=Roboto:wght@400&family=Source+Sans+3:wght@400&display=swap" rel="stylesheet">
<style>
  :root {
    --card-black: #000000;
    --brand-purple: #662d91;
    --brand-blue: #29abe2;
    --text-font: "Source Sans 3", sans-serif;
    --brand-font: "Roboto", sans-serif;
  }
  html, body {
    margin: 0;
    padding: 0;
    width: 1200px;
    height: 693px;
    overflow: hidden;
    background: var(--card-black);
  }
  .card {
    position: relative;
    width: 1200px;
    height: 693px;
    background: var(--card-black);
    overflow: hidden;
  }
  .top-band {
    position: absolute;
    left: 0; top: 0;
    width: 1200px; height: 36px;
    background: var(--brand-purple);
  }
  .staff {
    position: absolute;
    right: 81px;
    top: 70px;
    margin: 0;
    font-family: var(--text-font);
    font-weight: 400;
    font-size: 26px;
    line-height: 36px;
    letter-spacing: 0.3px;
    color: var(--brand-blue);
    text-align: right;
  }
  .staff span { display: block; }
  .brand-mark {
    position: absolute;
    left: 240px;
    top: 268px;
  }
  .brand-name {
    position: absolute;
    right: 81px;
    top: 318px;
    margin: 0;
    font-family: var(--brand-font);
    font-weight: 400;
    font-size: 53px;
    line-height: 53px;
    letter-spacing: -0.5px;
    color: var(--brand-purple);
    white-space: nowrap;
  }
  .tagline {
    position: absolute;
    right: 81px;
    top: 376px;
    margin: 0;
    font-family: var(--brand-font);
    font-weight: 400;
    font-size: 33px;
    line-height: 33px;
    color: var(--brand-blue);
    white-space: nowrap;
  }
  .divider {
    position: absolute;
    left: 0;
    top: 531px;
    width: 1118px;
    height: 3px;
    background: var(--brand-purple);
  }
  .contact {
    position: absolute;
    right: 88px;
    top: 549px;
    margin: 0;
    font-family: var(--text-font);
    font-style: normal;
    font-weight: 400;
    font-size: 24px;
    line-height: 34px;
    letter-spacing: 0.5px;
    color: var(--brand-blue);
    text-align: right;
    white-space: nowrap;
  }
  .contact span { display: block; }
</style>
</head>
<body>
  <main class="card">
    <div class="top-band"></div>

    <p class="staff">
      <span class="staff-name">Janet Colby FCA</span>
      <span class="staff-title">Principal Consultant</span>
    </p>

    <svg class="brand-mark" width="120" height="120" viewBox="0 0 120 120" aria-hidden="true">
      <circle cx="60" cy="60" r="52" fill="var(--brand-blue)"/>
    </svg>

    <h1 class="brand-name">HARBOR RIDGE ADVISORY</h1>
    <p class="tagline">FOUNDATIONS FOR YOUR MISSION</p>

    <div class="divider"></div>

    <address class="contact">
      <span>PO Box 87, Larkfield VIC 3148, Phone: 03 9871 2264 Mobile: 0412 846 309</span>
      <span>E-mail: janet@harborridgeadvisory.com.au</span>
      <span>Web: www.harborridgeadvisory.com.au&nbsp; Linked In: au.linkedin.com/in/janetcolbyhra/</span>
    </address>
  </main>
</body>
</html>
```